Dynamic Business Card for Sports Supplements Company

Hi! I'm looking for an awesome business card to match my existing sports supplement company. I have uploaded my current company logo and screenshot of the front page of my website.

I would like to have something dynamic and interesting and utilize the colors in the website - the reds and purples

The business card should be double sided and focus on a unique eye-catching design on the back and include all the relevant company info.

Most importantly, it should say somewhere: "Sign up on our website for a coupon code."

Target Market(s)

Mostly for women gym goers but it shouldn't be too feminine. It should be in keeping with the website design. It should flow and clearly be connected to it

Industry/Entity Type

Business

Contact Information for Business Card

Colleen M. Varga
CEO
CVarga@Vitalorexco.example
www.vitalorexco.example
555.014.3827
P.O. Box 48317
Fairhaven, Ohio 00000

Sign up on our website for a coupon code

Font styles to use
Serif
Sans Serif
Other font styles liked:
• Novecento font family and "Vitalorex" is in AR Destine font

Requirements
Must have
• One side should be a bold Vitalorex logo design. Even just the symbol itself may be o.k. (see attached file)

```html
<!DOCTYPE html>
<html lang="en">
<head>
<meta charset="utf-8">
<title>Vitalorex Business Card</title>
<link rel="stylesheet" href="https://fonts.googleapis.com/css2?family=Montserrat:wght@400;500;700&display=swap">
<style>
  :root {
    --brand-red: #ec1c24;
    --ink-black: #000000;
    --paper-white: #ffffff;
    --stage: #3a3a3a;
    --body-font: "Montserrat", Arial, sans-serif;
  }
  * { margin: 0; padding: 0; box-sizing: border-box; }
  html, body {
    width: 1200px;
    height: 855px;
    overflow: hidden;
    background: var(--stage);
    font-family: var(--body-font);
  }
  .card {
    position: absolute;
    left: 354px;
    width: 493px;
    overflow: hidden;
    box-shadow: 0 4px 14px rgba(0,0,0,0.45);
  }
  .card-front {
    top: 137px;
    height: 280px;
    background: var(--brand-red);
    color: var(--paper-white);
  }
  .front-wordmark {
    position: absolute;
    top: 116px;
    left: 0;
    width: 100%;
    text-align: center;
    font-size: 34px;
    font-weight: 700;
    letter-spacing: 1px;
  }
  .front-offer {
    position: absolute;
    top: 237px;
    left: 0;
    width: 100%;
    text-align: center;
    font-size: 12.5px;
    font-weight: 400;
  }
  .card-back {
    top: 430px;
    height: 288px;
    background: var(--paper-white);
  }
  .card-back svg.diagonal {
    position: absolute;
    inset: 0;
  }
  .contact {
    position: absolute;
    left: 26px;
    top: 120px;
    color: var(--paper-white);
    font-size: 12.5px;
    line-height: 1.35;
  }
  .contact-name {
    color: var(--brand-red);
    font-size: 18px;
    font-weight: 500;
    line-height: 1.15;
  }
  .contact-role { margin-bottom: 12px; }
  .contact-address { margin-bottom: 12px; }
  .contact-line {
    display: flex;
    align-items: center;
    gap: 5px;
  }
  .contact-line svg { width: 11px; height: 11px; flex: none; }
  .brand-block {
    position: absolute;
    left: 300px;
    top: 98px;
    width: 170px;
    text-align: center;
    color: var(--ink-black);
  }
  .brand-name {
    font-size: 28px;
    font-weight: 700;
    letter-spacing: 0.5px;
    line-height: 1;
  }
  .brand-tagline {
    font-size: 8.3px;
    font-weight: 500;
    letter-spacing: 0.4px;
    margin-top: 3px;
  }
</style>
</head>
<body>
  <section class="card card-front">
    <div class="front-wordmark">Vitalorex</div>
    <p class="front-offer">Sign up on our website for a coupon code</p>
  </section>

  <section class="card card-back">
    <svg class="diagonal" width="493" height="288" viewBox="0 0 493 288">
      <polygon points="0,0 164,0 315,288 0,288" fill="var(--ink-black)"/>
      <polygon points="167,0 172,0 324,288 319,288" fill="var(--brand-red)"/>
    </svg>

    <div class="contact">
      <div class="contact-name">Colleen M. Varga</div>
      <div class="contact-role">CEO</div>
      <div class="contact-address">P.O. Box 48317<br>Fairhaven, Ohio 00000</div>
      <div class="contact-line">
        <svg viewBox="0 0 12 12"><path d="M2 11 C1 7 4 2 9 1 L11 3 L8.5 4.5 L7 3.5 C5 4.5 4 6.5 4 8.5 L5.5 9 L4.5 11.5 Z" fill="var(--brand-red)"/></svg>
        <span>555.014.3827</span>
      </div>
      <div class="contact-line">
        <svg viewBox="0 0 12 12"><rect x="0.5" y="2.5" width="11" height="7" fill="var(--brand-red)"/><path d="M0.5 2.5 L6 7 L11.5 2.5" stroke="var(--ink-black)" stroke-width="0.9" fill="none"/></svg>
        <span>CVarga@Vitalorexco.example</span>
      </div>
      <div class="contact-line">
        <svg viewBox="0 0 12 12" fill="none" stroke="var(--brand-red)" stroke-width="1"><circle cx="6" cy="6" r="5"/><ellipse cx="6" cy="6" rx="2.2" ry="5"/><line x1="1" y1="6" x2="11" y2="6"/></svg>
        <span>www.vitalorexco.example</span>
      </div>
    </div>

    <div class="brand-block">
      <div class="brand-name">Vitalorex</div>
      <div class="brand-tagline">YOUR STRENGTH COMPANION</div>
    </div>
  </section>
</body>
</html>
```